Medical Cannabis company is looking for a LOGO design *

SILVER PETALWORKS (SP) is a new company in the Israeli medical cannabis industry. We will engage in PREMIUM medical cannabis growing and cultivation and also manufacturing of HIGH-END cannabis based medical products.
the design should reflect luxury, high-end and Pharma-grade products.
the design should use color GOLD and NOT using the famous cannabis leaf !

Target Market(s)

international medical cannabis Pharmaceutical companies
and of course local and international patients

Contact Information for Business Card

Yoav Ben-Ami
Founder and CEO

Silver Petalworks
Medical grade cannabis

yoavbenami@mailnest.example
972-52-3186907

Colors
ffc214
fbed22

Requirements
Must have
• clean and simple
• luxury
• gold !!
• (can also have green for Cannabis and/or blue for Pharma)
Should not have
• cannabis leaf

```html
<!DOCTYPE html>
<html lang="en">
<head>
<meta charset="UTF-8">
<title>Silver Petalworks — Business Card</title>
<link rel="stylesheet" href="https://fonts.googleapis.com/css2?family=Cinzel:wght@600&family=Lato:wght@400&family=Montserrat:wght@400&display=swap">
<style>
  :root {
    --backdrop: #b1b1b1;
    --card: #050a1d;
    --gold: #ffc214;
    --white: #ffffff;
    --muted: #c9ccd6;
    --rule: #3a4058;
  }
  html, body {
    margin: 0;
    padding: 0;
    width: 1200px;
    height: 900px;
    overflow: hidden;
    background: var(--backdrop);
  }
  .canvas {
    position: relative;
    width: 1200px;
    height: 900px;
  }
  .card {
    position: absolute;
    top: 306px;
    width: 438px;
    height: 271px;
    border-radius: 11px;
    background: var(--card);
    overflow: hidden;
  }
  .card--front { left: 150px; }
  .card--back { left: 610px; }

  .brand {
    position: absolute;
    right: 27px;
    top: 36px;
    text-align: right;
  }
  .brand__mark {
    font-family: "Cinzel", serif;
    font-weight: 600;
    font-size: 50px;
    line-height: 1;
    color: var(--gold);
    margin-right: 48px;
  }
  .brand__name {
    font-family: "Cinzel", serif;
    font-weight: 600;
    font-size: 17px;
    line-height: 1;
    color: var(--gold);
    margin-top: 15px;
    white-space: nowrap;
  }
  .brand__tagline {
    font-family: "Montserrat", sans-serif;
    font-size: 8.5px;
    letter-spacing: 2.3px;
    color: var(--muted);
    margin-top: 3px;
    margin-right: -2px;
    white-space: nowrap;
  }

  .person {
    position: absolute;
    left: 26px;
    top: 156px;
    width: 382px;
  }
  .person__name {
    font-family: "Cinzel", serif;
    font-weight: 600;
    font-size: 17px;
    color: var(--gold);
    line-height: 1;
  }
  .person__role {
    display: flex;
    align-items: center;
    margin-top: 6px;
    font-family: "Lato", sans-serif;
    font-size: 12px;
    color: var(--white);
  }
  .person__rule {
    flex: 1;
    height: 1px;
    background: var(--rule);
    margin-left: 12px;
  }

  .contact {
    position: absolute;
    right: 27px;
    top: 211px;
    font-family: "Lato", sans-serif;
    color: var(--white);
    text-align: right;
  }
  .contact__row {
    display: flex;
    justify-content: flex-end;
    align-items: center;
    gap: 5px;
    line-height: 20px;
  }
  .contact__row--phone { font-size: 14px; }
  .contact__row--email { font-size: 12.5px; }
  .contact__icon { width: 10px; height: 10px; fill: var(--gold); }

  .back-mark {
    position: absolute;
    left: 262px;
    top: 172px;
    font-family: "Cinzel", serif;
    font-weight: 600;
    font-size: 30px;
    line-height: 1;
    color: var(--gold);
  }
</style>
</head>
<body>
<div class="canvas">
  <section class="card card--front">
    <div class="brand">
      <div class="brand__mark">SP</div>
      <div class="brand__name">Silver Petalworks</div>
      <div class="brand__tagline">MEDICAL GRADE CANNABIS</div>
    </div>

    <div class="person">
      <div class="person__name">Yoav Ben-Ami</div>
      <div class="person__role">Founder and CEO<span class="person__rule"></span></div>
    </div>

    <div class="contact">
      <div class="contact__row contact__row--phone">
        <span>972-52-3186907</span>
        <svg class="contact__icon" viewBox="0 0 24 24" aria-hidden="true"><path d="M6.6 10.8a15.1 15.1 0 0 0 6.6 6.6l2.2-2.2a1 1 0 0 1 1-.25 11.4 11.4 0 0 0 3.6.57 1 1 0 0 1 1 1V20a1 1 0 0 1-1 1A17 17 0 0 1 3 4a1 1 0 0 1 1-1h3.5a1 1 0 0 1 1 1c0 1.25.2 2.45.57 3.57a1 1 0 0 1-.25 1z"/></svg>
      </div>
      <div class="contact__row contact__row--email">
        <span>yoavbenami@mailnest.example</span>
        <svg class="contact__icon" viewBox="0 0 24 24" aria-hidden="true"><path d="M2 5h20v14H2z M3 6l9 7 9-7" stroke="#050a1d" stroke-width="1.6"/></svg>
      </div>
    </div>
  </section>

  <section class="card card--back">
    <div class="back-mark">SP</div>
  </section>
</div>
</body>
</html>
```